Political Marketing Company - Valentine's Day Card - Huge!

We need a 5"x7" Valentine's Day card in the style of the attached images. We want it to be slightly cartoon-y, but heartfelt. Copy for card is as follows, with direction:Outside: My love for you is…(Text only, bold san-serif font, light background)Inside: HUUUUUUUGE! (graphic of Harold Benning with hands out spanning both inside pages with “HUUUUUUUUGE!” above Benning, big, bold san serif font).

Font styles to use
Serif

```html
<!DOCTYPE html>
<html lang="en">
<head>
<meta charset="utf-8">
<title>Valentine's Card – My Love For You Is Huge</title>
<link rel="stylesheet" href="https://fonts.googleapis.com/css2?family=Poppins:wght@800;900&display=swap">
<style>
  :root {
    --page-bg: #e9e6e6;
    --card-white: #ffffff;
    --pink-light: #e6b4b4;
    --pink-mid: #e29c9c;
    --pink-deep: #dc8080;
    --pink-glow: #eec6c6;
    --type-white: #ffffff;
    --type-shadow: #4b3a78;
    --frame-line: #2c3b5a;
    --figure-navy: #1f2d4f;
    --figure-skin: #f2b277;
  }
  * { box-sizing: border-box; margin: 0; padding: 0; }
  html, body {
    width: 1200px; height: 899px; overflow: hidden;
    background: var(--page-bg);
    font-family: "Poppins", "Helvetica Neue", Arial, sans-serif;
  }
  .canvas { position: relative; width: 1200px; height: 899px; }

  .card {
    position: absolute;
    width: 560px; height: 400px;
    overflow: hidden;
    box-shadow: 0 10px 28px rgba(0,0,0,0.22);
  }

  /* Outside of card */
  .card--outside { left: 40px; top: 40px; display: flex; }
  .outside__back {
    width: 48%; height: 100%;
    background: var(--card-white);
    position: relative;
  }
  .outside__box {
    position: absolute; left: 150px; bottom: 40px;
    width: 110px; height: 80px;
    border: 1.5px solid var(--frame-line);
  }
  .outside__front {
    width: 52%; height: 100%;
    position: relative;
    background: var(--pink-light);
  }
  .outside__front svg { position: absolute; inset: 0; }
  .outside__headline {
    position: absolute; left: 70px; top: 36px;
    color: var(--type-white);
    font-weight: 800; font-size: 44px; line-height: 1.08;
    text-transform: uppercase; letter-spacing: 0.5px;
  }

  /* Inside of card */
  .card--inside { left: 600px; top: 459px; background: var(--pink-light); }
  .card--inside svg.inside__rings { position: absolute; inset: 0; }
  .inside__headline {
    position: absolute; left: 0; right: 0; top: 70px;
    text-align: center;
    color: var(--type-white);
    font-weight: 900; font-size: 70px; letter-spacing: -1px;
    text-shadow: 4px 5px 0 var(--type-shadow);
  }
  .inside__figure {
    position: absolute; left: 60px; right: 40px; bottom: 0; height: 195px;
    background: linear-gradient(180deg, var(--figure-skin) 0%, var(--figure-navy) 70%);
    border-radius: 90px 90px 0 0;
    opacity: 0.9;
  }
</style>
</head>
<body>
<main class="canvas">

  <section class="card card--outside" aria-label="Card outside">
    <div class="outside__back">
      <div class="outside__box"></div>
    </div>
    <div class="outside__front">
      <svg width="291" height="400" viewBox="0 0 291 400" aria-hidden="true">
        <circle cx="250" cy="170" r="240" fill="var(--pink-mid)"/>
        <circle cx="300" cy="230" r="150" fill="var(--pink-deep)" opacity="0.55"/>
      </svg>
      <h1 class="outside__headline">My<br>Love<br>For<br>You<br>Is…</h1>
    </div>
  </section>

  <section class="card card--inside" aria-label="Card inside">
    <svg class="inside__rings" width="560" height="400" viewBox="0 0 560 400" aria-hidden="true">
      <circle cx="0" cy="0" r="60" fill="var(--pink-glow)"/>
      <ellipse cx="290" cy="300" rx="300" ry="240" fill="var(--pink-mid)"/>
      <ellipse cx="300" cy="330" rx="200" ry="170" fill="var(--pink-deep)" opacity="0.6"/>
    </svg>
    <h2 class="inside__headline">HUUUUUUUGE!</h2>
    <div class="inside__figure" role="img" aria-label="Cartoon illustration of Harold Benning in a navy suit with arms spread wide"></div>
  </section>

</main>
</body>
</html>
```